디자인 카테고리
브로셔/리플렛 (공공기관 업종)
브랜드 소개
푸른 새벽길은 청솔다온회종의 종지와 자비정신에 기반하며 나눔을 실천하는 기부문화를 확산시키고 투명성을 바탕으로 소외계층과 각종 공익활동에 필요한 지원에 도움을 주고자 설립되었습니다.
이에 푸른 새벽길은 목적을 달성하기 위해 다음과 같은 사업을 전개합니다.
- 기부문화 확산을 위한 대국민 홍보․조사․정책연구
- 개인, 단체, 기업의 지정기탁에 따른 공익기금 및 특정주제를 갖는 목적형 기금조성
- 사회복지모금사업, 모금재원의 운용․관리 및 배분사업
- 재난재해구호, 해외난민구호 등 인도적 지원 사업
- 민족화합과 협력을 위한 공동체 회복 지원 사업
- 소외계층의 삶의 질 향상을 위한 공익사업 지원
- 공공의 삶과 직결된 환경보호에 대한 시민의식 고취사업
- 기타 법인의 목적사업 달성에 필요한 사업

```html
<!DOCTYPE html>
<html lang="ko">
<head>
<meta charset="utf-8">
<title>푸른새벽길 후원 리플렛</title>
<link href="https://fonts.googleapis.com/css2?family=Noto+Sans+KR:wght@300;400;500;700;900&display=swap" rel="stylesheet">
<style>
:root{
  --bg:#ebe9e5;
  --paper:#ffffff;
  --orange:#e8792a;
  --gold:#efa52c;
  --green:#8fba3c;
  --green-line:#b9d47f;
  --ink:#4a4a4a;
  --ink-soft:#7a7a7a;
  --rule:#d9d9d9;
}
*{box-sizing:border-box;margin:0;padding:0}
html,body{width:1200px;height:1200px;overflow:hidden}
body{background:var(--bg);font-family:"Noto Sans KR",sans-serif;color:var(--ink)}
.leaflet{position:absolute;left:60px;top:190px;width:1080px;height:820px;display:flex;box-shadow:0 12px 30px rgba(0,0,0,.12)}
.panel{position:relative;width:360px;height:820px;background:var(--paper);overflow:hidden}
.panel + .panel{border-left:1px solid #e4e4e4}

/* 사업 소개 */
.program-tab{background:var(--orange);color:#fff;font-weight:700;font-size:17px;padding:12px 26px;line-height:1.35}
.program-body{font-size:12px;line-height:1.7;color:var(--ink);padding:10px 26px 12px}
.program-title{color:var(--orange);font-weight:700;font-size:16px;line-height:1.35;padding:6px 26px 0}
.program-box{margin:4px 26px 0;background:var(--orange);color:#fff;padding:12px 16px}
.program-box h3{font-size:16px;font-weight:700;margin-bottom:6px}
.program-box p{font-size:12px;line-height:1.65}
.program-note{color:var(--orange);font-size:12px;line-height:1.7;padding:12px 26px 0;font-weight:500}

.apply-form{margin:16px 26px 0;border-top:2px solid var(--orange)}
.apply-form h3{font-size:14px;font-weight:700;color:var(--ink);padding:8px 0 4px}
.apply-row{display:flex;border-bottom:1px solid var(--rule);font-size:11px;height:27px;align-items:center}
.apply-row .field{width:78px;color:var(--ink);font-weight:500;padding-left:4px;border-right:1px solid var(--rule);height:100%;display:flex;align-items:center}
.apply-row .value{padding-left:10px;color:var(--ink-soft);display:flex;gap:14px;align-items:center}
.box{display:inline-block;width:9px;height:9px;border:1px solid var(--ink-soft);margin-right:4px;vertical-align:-1px}

/* 후원 방법 */
.support-head{display:flex;gap:16px;padding:28px 22px 16px;align-items:flex-start}
.support-title{color:var(--green);font-size:30px;font-weight:700;line-height:1.15;white-space:nowrap}
.support-intro{font-size:10.5px;line-height:1.6;color:var(--ink-soft);padding-top:4px}
.method-grid{display:grid;grid-template-columns:repeat(3,1fr);gap:6px;padding:0 22px}
.method{border:1px solid var(--green-line);background:var(--paper);text-align:center;padding:10px 4px 8px;font-size:10.5px;line-height:1.45}
.method svg{width:34px;height:34px;display:block;margin:0 auto 6px}
.method-wide{display:grid;grid-template-columns:1fr 1fr;gap:6px;padding:6px 22px 0}
.method-wide .method{display:flex;align-items:center;gap:6px;text-align:left;padding:10px 8px}
.method-wide .method svg{margin:0;flex:none}
.method strong{color:var(--ink);font-weight:700}
.channels{list-style:none;padding:18px 22px 0}
.channels li{display:flex;align-items:center;font-size:10.5px;padding:4px 0;border-bottom:1px dotted var(--rule)}
.channels .dot{width:12px;height:12px;border-radius:50%;background:var(--green);margin-right:8px;flex:none}
.channels .label{width:70px;color:var(--ink)}
.channels .url{margin-left:auto;color:var(--ink-soft)}
.join-band{position:absolute;left:0;right:0;top:470px;height:260px;background:var(--green);color:#fff;padding:38px 24px 0}
.join-band h2{font-size:21px;font-weight:700;line-height:1.35}
.join-band p{font-size:19px;font-weight:300;line-height:1.4;margin-top:14px}
.footer{position:absolute;left:0;right:0;bottom:0;height:90px;padding:18px 22px;font-size:9.5px;line-height:1.7;color:var(--ink-soft)}
.footer strong{color:var(--ink);font-weight:700}

/* 표지 */
.cover-top{position:relative;height:330px;background:var(--gold);color:#fff;padding:30px 26px}
.cover-title{font-size:34px;font-weight:700;line-height:1.22;margin-top:40px}
.cover-sub{font-size:12px;line-height:1.6;margin-top:28px}
.brand{position:absolute;top:30px;right:24px;display:flex;align-items:center;gap:6px;font-size:13px;font-weight:700;color:#fff}
.brand .mark{width:14px;height:14px;border-radius:50%;background:#fff}
.cover-photo{height:490px;background:linear-gradient(180deg,#7d8a5a 0%,#9c8f72 45%,#b49a78 70%,#7a6a55 100%)}
</style>
</head>
<body>
<main class="leaflet">

  <section class="panel programs">
    <div class="program-tab">국내 저소득가정<br>지원사업</div>
    <p class="program-body">경제적 어려움으로 생계가 곤란한 저소득가정에 생계비와 의료비, 교육비를 지원하여 자립의 기반을 함께 만들어 갑니다.</p>
    <h3 class="program-title">사회복지단체 및<br>NGO 지원사업</h3>
    <p class="program-body">지역사회 복지단체와 비영리 민간단체의 공익활동을 지원하여 소외된 이웃에게 도움이 고루 닿도록 협력합니다.</p>
    <div class="program-box">
      <h3>북한 지원사업</h3>
      <p>민족화합과 협력을 위해 식량과 의약품, 생활물품을 지원하며 공동체 회복을 위한 교류를 이어 갑니다.</p>
    </div>
    <p class="program-note">푸른새벽길은 투명한 모금과 배분으로 나눔의 가치를 지키며, 보내주신 후원금은 꼭 필요한 곳에 소중히 쓰입니다.</p>

    <form class="apply-form">
      <h3>후원신청서</h3>
      <div class="apply-row"><span class="field">성명</span><span class="value"></span></div>
      <div class="apply-row"><span class="field">연락처</span><span class="value"></span></div>
      <div class="apply-row"><span class="field">주소</span><span class="value"></span></div>
      <div class="apply-row"><span class="field">후원금액</span><span class="value"><span><i class="box"></i>1만원</span><span><i class="box"></i>3만원</span><span><i class="box"></i>기타</span></span></div>
      <div class="apply-row"><span class="field">납부방법</span><span class="value"><span><i class="box"></i>자동이체</span><span><i class="box"></i>지로</span></span></div>
      <div class="apply-row"><span class="field">서명</span><span class="value"></span></div>
    </form>
  </section>

  <section class="panel support">
    <header class="support-head">
      <h2 class="support-title">후원<br>방법</h2>
      <p class="support-intro">푸른새벽길은 여러분의 정성을 모아 국내외 소외된 이웃에게 희망을 전합니다. 작은 나눔이 큰 변화를 만듭니다.</p>
    </header>
    <div class="method-grid">
      <div class="method">
        <svg viewBox="0 0 34 34" aria-hidden="true"><circle cx="17" cy="17" r="16" fill="none" stroke="#8fba3c" stroke-width="1.5"/><path d="M11 10c1-1 3-1 3.5 0l1.5 3c.3.7 0 1.4-.6 1.8l-1 .7c.8 2 2.3 3.5 4.2 4.3l.7-1c.4-.6 1.2-.9 1.8-.6l3 1.5c1 .5 1 2.5 0 3.5-1.5 1.5-4 1.8-7-.4-3-2.2-5.3-5.3-6-8-.5-2 0-3.8.9-4.8z" fill="#8fba3c"/></svg>
        <strong>02-555-0142</strong> 로<br>후원신청 및 문의
      </div>
      <div class="method">
        <svg viewBox="0 0 34 34" aria-hidden="true"><rect x="9" y="5" width="16" height="24" fill="none" stroke="#8fba3c" stroke-width="1.6"/><path d="M12 11h10M12 15h10M12 19h10M12 23h6" stroke="#8fba3c" stroke-width="1.5"/></svg>
        후원신청서 작성<br>후 우편으로 발송
      </div>
      <div class="method">
        <svg viewBox="0 0 34 34" aria-hidden="true"><path d="M5 17L17 6l12 11" fill="none" stroke="#8fba3c" stroke-width="1.8"/><path d="M9 15v13h16V15" fill="none" stroke="#8fba3c" stroke-width="1.8"/><rect x="14.5" y="20" width="5" height="8" fill="#8fba3c"/></svg>
        <strong>saebyeokgil.org</strong><br>가입 후 후원하기
      </div>
    </div>
    <div class="method-wide">
      <div class="method">
        <svg viewBox="0 0 34 34" aria-hidden="true"><rect x="6" y="9" width="22" height="16" rx="3" fill="none" stroke="#8fba3c" stroke-width="1.6"/><path d="M10 13h14M10 17h14M10 21h8" stroke="#8fba3c" stroke-width="1.4"/></svg>
        <span><strong>060-555-0190</strong><br>* ARS 전화후원<br>한 통에 5000원</span>
      </div>
      <div class="method">
        <svg viewBox="0 0 34 34" aria-hidden="true"><path d="M17 27s-10-6-10-13a5 5 0 0 1 10-1 5 5 0 0 1 10 1c0 7-10 13-10 13z" fill="none" stroke="#8fba3c" stroke-width="1.8"/></svg>
        <span>매월 <strong>30,000원</strong><br>해외빈곤아동과<br>1:1 결연 후원</span>
      </div>
    </div>
    <ul class="channels">
      <li><span class="dot"></span><span class="label">홈페이지</span><span class="url">www.saebyeokgil.org</span></li>
      <li><span class="dot"></span><span class="label">블로그</span><span class="url">blog.saebyeokgil.org</span></li>
      <li><span class="dot"></span><span class="label">소식채널</span><span class="url">news.saebyeokgil.org</span></li>
      <li><span class="dot"></span><span class="label">커뮤니티</span><span class="url">together.saebyeokgil.org</span></li>
    </ul>
    <div class="join-band">
      <h2>푸른새벽길과<br>함께 해주세요!</h2>
      <p>희망과 행복을<br>지구촌 곳곳에<br>감동으로 나누겠습니다.</p>
    </div>
    <footer class="footer">
      <strong>재단법인 푸른새벽길</strong> 서울시 중구 새벽길 12, 3층<br>
      Tel. 02-555-0142 &nbsp; Fax. 02-555-0143<br>
      E-mail. hello@saebyeokgil.org
    </footer>
  </section>

  <section class="panel cover">
    <div class="cover-top">
      <div class="brand"><span class="mark"></span>푸른새벽길</div>
      <h1 class="cover-title">당신의<br>나눔이<br>만듭니다.</h1>
      <p class="cover-sub">오늘보다 더 나은 내일을<br>오늘보다 더 행복한 웃음을<br>오늘보다 더 아름다운 세상을</p>
    </div>
    <div class="cover-photo" role="img" aria-label="봉사자와 마을 아이들, 주민들이 흙벽 집 앞에 함께 앉아 있는 사진"></div>
  </section>

</main>
</body>
</html>
```